Southport Billboard for Hiring more CDL drivers

I need a catch design for a bill board (size 10ft by 36 ft) to catch the attention for semi truck drivers.
In the design I want it to include:
-My company logo along with my website(brisklanefreighters.com) and my number(503-217-6095) for contact info.
-I also need it to say earn up to $90,000 a year
-I will send a few photos to choose from
-I need the logo to look clean and simple! I don't want it to be cluttered just clean, simple and catchy.!

Target Market(s)

CDL Class A holders
Semi Truck Drivers

Industry/Entity Type

Trucking Company

Font styles to use
Other font styles liked:
• a font to match my logo

Requirements
Must have
• "Make up to $90,000"
"brisklanefreighters.com"
"503-217-6095"

```html
<!DOCTYPE html>
<html lang="en">
<head>
<meta charset="utf-8">
<title>Brisk Lane Freighters – Driver Hiring Billboard</title>
<link rel="stylesheet" href="https://fonts.googleapis.com/css2?family=Anton&family=Barlow:wght@600;700;800&display=swap">
<style>
  :root {
    --stage: #e9eaea;
    --ink-dark: #23251f;
    --white: #ffffff;
    --header-dark: #262823;
    --hill: #4a4a40;
    --sand: #9a8f76;
    --water: #7d8586;
    --truck-blue: #3f7fb0;
    --loader-yellow: #c9a227;
    --road: #5e5f61;
    --road-edge: #47484a;
  }
  html, body {
    margin: 0;
    padding: 0;
    width: 1200px;
    height: 706px;
    overflow: hidden;
    background: var(--stage);
  }
  .billboard {
    position: absolute;
    left: 20px;
    top: 192px;
    width: 1160px;
    height: 322px;
    overflow: hidden;
    background: var(--header-dark);
    font-family: "Barlow", "Arial Narrow", sans-serif;
    color: var(--white);
  }
  .billboard__photo {
    position: absolute;
    left: 0;
    right: 0;
    top: 150px;
    bottom: 0;
    background:
      radial-gradient(ellipse 150px 60px at 27% 62%, rgba(63,127,176,0.85), rgba(63,127,176,0) 100%),
      radial-gradient(ellipse 130px 55px at 62% 55%, rgba(201,162,39,0.85), rgba(201,162,39,0) 100%),
      linear-gradient(180deg,
        var(--hill) 0%,
        var(--sand) 30%,
        var(--water) 48%,
        var(--road) 72%,
        var(--road-edge) 100%);
    border-top: 2px solid rgba(255,255,255,0.25);
  }
  .brand {
    position: absolute;
    left: 34px;
    top: 24px;
    margin: 0;
    font-family: "Anton", "Impact", sans-serif;
    font-weight: 400;
    font-size: 56px;
    line-height: 1.0;
    letter-spacing: 0.5px;
    color: var(--white);
    text-transform: uppercase;
  }
  .offer {
    position: absolute;
    left: 320px;
    top: 36px;
    width: 290px;
    height: 106px;
    box-sizing: border-box;
    border: 2px solid var(--white);
    z-index: 1;
  }
  .offer__tag {
    position: absolute;
    left: 50%;
    transform: translateX(-50%);
    background: var(--header-dark);
    padding: 0 8px;
    font-weight: 700;
    font-size: 24px;
    line-height: 28px;
    white-space: nowrap;
    text-transform: uppercase;
  }
  .offer__tag--top { top: -16px; }
  .offer__tag--bottom { bottom: -16px; }
  .offer__amount {
    position: absolute;
    left: 0;
    right: 0;
    top: 18px;
    text-align: center;
    font-weight: 800;
    font-size: 62px;
    line-height: 66px;
  }
  .contact__phone {
    position: absolute;
    right: 22px;
    top: 14px;
    font-weight: 700;
    font-size: 74px;
    line-height: 80px;
    letter-spacing: 0.5px;
  }
  .contact__web {
    position: absolute;
    left: 800px;
    right: 0;
    top: 101px;
    height: 38px;
    background: var(--white);
    color: var(--ink-dark);
    font-weight: 700;
    font-size: 20px;
    line-height: 38px;
    letter-spacing: 1.5px;
    text-align: center;
    text-transform: uppercase;
    z-index: 1;
  }
</style>
</head>
<body>
  <section class="billboard" aria-label="Brisk Lane Freighters driver hiring billboard">
    <div class="billboard__photo" role="img" aria-label="Photo of a blue semi truck hauling a yellow wheel loader on a flatbed trailer along a highway, with a sandy shore and dark hillside behind"></div>

    <h1 class="brand">Brisk Lane<br>Freighters</h1>

    <div class="offer">
      <span class="offer__tag offer__tag--top">Earn up to</span>
      <div class="offer__amount">$90,000</div>
      <span class="offer__tag offer__tag--bottom">A year</span>
    </div>

    <div class="contact__phone">503-217-6095</div>
    <div class="contact__web">brisklanefreighters.com</div>
  </section>
</body>
</html>
```